LKT business card design

Coastal Guard Auxiliary Kin Services exists to provide timely and relevant programs and services to assist commanders with their role to ensure their assigned Families (Soldiers, spouses, children, significant others) have the highest possible level of well-being, and are the "ready" (for deployment, family separation, and self-sufficiency during that separation). We accomplish this task through several functional areas: Leadership (Director), Coordination (Coordinator--coordinates a variety of human services, staff sections, sister agencies, etc. to offer training and support), unit Family Readiness Programs, Junior Learner and Campus Aid, Bereaved Contact Network, Lantern Path Initiative (deployment and reintegration training), Recovery Care (for wounded warriors), Crisis Intervention, and Prevention Education and Training. Our aim is to demonstrate "Kin Above All" in everything we do, because Family Readiness improves Soldier Readiness which improves Army Readiness.

Folks, I've tried to upload the logos I mentioned, with not luck. You can get a look at one version of the Guard Auxiliary Kin Services logo at www.gaks-example.org.

Reason: Extendinig a couple days because I've not yet had any sucess uploading logos I mention in the brief. Hoping to crack the nut on that soon Thanks for your patient work.

Target Market(s)

Army Reserve Commanders, First Sergeants, Adult & Youth Volunteers & Family Members who are called to contribute to Whole Guard Kin readiness by being skilled at handling the challendes of deployment, family separation, and the self-sufficiency required when their Soldier deploys (e.g., fulfilling the Soldiers roles on the homefront while he or she is away)

Industry/Entity Type

Training

Contact Information for Business Card

Dr. Marcus T. Holloway, Director
Family Programs, 4th RDG, CGAWEST
2846 Ridge Lane
Honolulu, HI 96502-4718
808-555-0172 ext. 4820
BB: 808-555-0639
marcus.t.holloway7.staff@postbox-example.net

Requirements
Must have
• Family Programs Logo with text
Nice to have
• 4th RDG and CGAWEST Logo
Should not have
• old GAKS Logo (Green, blue globe with family silhouette)

```html
<!DOCTYPE html>
<html lang="en">
<head>
<meta charset="utf-8">
<title>LKT Business Card – Dr. Marcus T. Holloway</title>
<link href="https://fonts.googleapis.com/css2?family=Alegreya+Sans:wght@400&display=swap" rel="stylesheet">
<style>
  :root {
    --card-bg: #ffffff;
    --ink: #1a1a1a;
    --rail-green: #1f8a2e;
    --rope-tone-light: #e6e6e6;
    --rope-tone-dark: #bdbdbd;
    --burst-green: #2f9a3a;
    --unit-red: #d8252f;
    --region-blue: #2b4fa8;
    --kin-green: #9fdc8a;
  }
  * { margin: 0; padding: 0; box-sizing: border-box; }
  html, body {
    width: 1200px;
    height: 693px;
    overflow: hidden;
    background: var(--card-bg);
  }
  .card {
    position: relative;
    width: 1200px;
    height: 693px;
    background: var(--card-bg);
    font-family: "Alegreya Sans", "Trebuchet MS", sans-serif;
    color: var(--ink);
  }
  .frame {
    position: absolute;
    inset: 0;
  }
  .text-block {
    position: absolute;
    left: 90px;
    line-height: 1;
    white-space: nowrap;
  }
  .holder-name { top: 104px; font-size: 50px; }
  .holder-title { top: 163px; font-size: 32px; }
  .address-street { top: 330px; font-size: 34px; }
  .address-city { top: 395px; font-size: 34px; }
  .contact-email { top: 557px; font-size: 34px; }
  .contact-phone { top: 626px; font-size: 34px; }

  .unit-mark, .region-mark, .program-mark {
    position: absolute;
    text-align: center;
    line-height: 1.1;
    white-space: nowrap;
  }
  .unit-mark { left: 1042px; top: 140px; width: 130px; font-size: 26px; }
  .region-mark { left: 1028px; top: 515px; width: 130px; font-size: 24px; }
  .program-mark {
    left: 706px; top: 300px; width: 490px; font-size: 36px;
  }
</style>
</head>
<body>
<main class="card">
  <svg class="frame" width="1200" height="693" viewBox="0 0 1200 693" xmlns="http://www.w3.org/2000/svg">
    <defs>
      <linearGradient id="rope-h" x1="0" y1="0" x2="0" y2="1">
        <stop offset="0" stop-color="var(--rope-tone-light)"/>
        <stop offset="0.5" stop-color="var(--rope-tone-dark)"/>
        <stop offset="1" stop-color="var(--rope-tone-light)"/>
      </linearGradient>
      <linearGradient id="rope-v" x1="0" y1="0" x2="1" y2="0">
        <stop offset="0" stop-color="var(--rope-tone-light)"/>
        <stop offset="0.5" stop-color="var(--rope-tone-dark)"/>
        <stop offset="1" stop-color="var(--rope-tone-light)"/>
      </linearGradient>
    </defs>

    <rect class="rope-top" x="60" y="28" width="985" height="46" fill="url(#rope-h)" role="img" aria-label="Twisted rope ornament along the top edge"/>
    <rect class="rope-left" x="28" y="60" width="52" height="620" fill="url(#rope-v)" role="img" aria-label="Twisted rope ornament along the left edge"/>

    <line class="rail-top" x1="43" y1="51" x2="1045" y2="51" stroke="var(--rail-green)" stroke-width="6"/>
    <line class="rail-left" x1="53" y1="51" x2="53" y2="678" stroke="var(--rail-green)" stroke-width="6"/>

    <circle class="corner-burst" cx="45" cy="50" r="34" fill="var(--burst-green)" role="img" aria-label="Green starburst ornament at the top-left corner"/>

    <circle class="unit-disc" cx="1107" cy="68" r="62" fill="var(--unit-red)"/>
    <circle class="program-disc" cx="950" cy="345" r="130" fill="var(--kin-green)"/>
    <circle class="region-disc" cx="1093" cy="618" r="58" fill="var(--region-blue)"/>
  </svg>

  <div class="text-block holder-name">Dr. Marcus T. Holloway</div>
  <div class="text-block holder-title">Director, Family Programs, 4th RDG, CGAWEST</div>

  <div class="text-block address-street">2846 Ridge Lane</div>
  <div class="text-block address-city">Honolulu, HI 96502-4718</div>

  <div class="text-block contact-email">marcus.t.holloway7.staff@postbox-example.net</div>
  <div class="text-block contact-phone">808-555-0172 ext. 4820 BB: 808-555-0639</div>

  <div class="unit-mark">4th RDG</div>
  <div class="program-mark">Guard Auxiliary<br>Kin Services</div>
  <div class="region-mark">CGAWEST</div>
</main>
</body>
</html>
```